Accounting Business needs double sided DL flyer design

We need a double sided DL flyer designed,
Front side with logo, web address and our short intro.
Backside to have a list of services.
Our colours are blue and a concrete grey colour. Look at our website for a feel for our colour scheme.
www.tallowbrookventures.com.au
I have included the pic from our website to possibly use but we are also open to new creative ideas.
Target Market(s)
Our target market are proactive business owners, particularly in the wine and hospitality industry.
Industry/Entity Type
Business
Look and feel

```html
<!DOCTYPE html>
<html lang="en">
<head>
<meta charset="utf-8">
<title>Tallowbrook Ventures – DL Flyer</title>
<link rel="stylesheet" href="https://fonts.googleapis.com/css2?family=Lato:wght@300;400;700&display=swap">
<style>
  :root{
    --page-bg:#ecedef;
    --brand-blue:#1c4789;
    --brand-blue-deep:#0c2757;
    --accent-light:#dcebf8;
    --concrete:#5e5f61;
    --text-light:#ffffff;
    --icon-blue:#2f6fc0;
  }
  *{margin:0;padding:0;box-sizing:border-box}
  html,body{width:1200px;height:1169px;overflow:hidden}
  body{background:var(--page-bg);font-family:"Lato",sans-serif;position:relative}
  .flyer{position:absolute;top:94px;width:447px;height:940px;box-shadow:0 4px 14px rgba(0,0,0,.25);overflow:hidden}
  .flyer--front{left:120px}
  .flyer--back{left:638px}
  .flyer__bg{position:absolute;inset:0;width:447px;height:940px;display:block}
  .brand{position:absolute;top:0;left:0;width:447px;height:160px;display:flex;align-items:center;justify-content:center;gap:12px}
  .brand__mark{width:30px;height:30px;background:var(--brand-blue)}
  .brand__name{font-weight:700;font-size:25px;letter-spacing:1.5px;color:var(--brand-blue);text-transform:uppercase}
  .intro{position:absolute;top:578px;left:0;width:447px;text-align:center;color:var(--text-light);font-weight:300;font-size:24px;line-height:41px;text-transform:uppercase}
  .contact{position:absolute;left:27px;top:864px;color:var(--text-light);font-weight:300;font-size:21.5px;line-height:29px}
  .services__title{position:absolute;top:212px;left:0;width:447px;text-align:center;color:var(--text-light);font-weight:400;font-size:26px;letter-spacing:.5px}
  .services__list{position:absolute;top:280px;left:48px;list-style:none}
  .service{display:flex;align-items:center;height:47.3px;color:var(--text-light);font-weight:300;font-size:20.5px}
  .service__icon{width:35px;height:35px;margin-right:15px;flex:none}
</style>
</head>
<body>

<section class="flyer flyer--front">
  <svg class="flyer__bg" viewBox="0 0 447 940">
    <defs>
      <linearGradient id="hdrF" x1="0" x2="1"><stop offset="0" stop-color="#e3e4e6"/><stop offset=".55" stop-color="#ffffff"/><stop offset="1" stop-color="#e3e4e6"/></linearGradient>
      <linearGradient id="blueF" x1="0" y1="0" x2="1" y2="1"><stop offset="0" stop-color="#1c4789"/><stop offset="1" stop-color="#0c2757"/></linearGradient>
      <linearGradient id="photoF" x1="0" y1="0" x2="1" y2="1"><stop offset="0" stop-color="#d7d8d8"/><stop offset=".6" stop-color="#b7b9ba"/><stop offset="1" stop-color="#8e9093"/></linearGradient>
    </defs>
    <rect width="447" height="150" fill="url(#hdrF)"/>
    <rect y="150" width="447" height="400" fill="url(#photoF)" role="img" aria-label="Photo of concrete stairs rising along a grey wall"/>
    <polygon points="0,518 447,460 447,478 0,540" fill="#dcebf8"/>
    <polygon points="300,478 447,458 447,463 300,481" fill="#3a3b3d"/>
    <polygon points="0,538 447,476 447,858 0,810" fill="url(#blueF)"/>
    <polygon points="0,808 447,852 447,892 0,816" fill="#dcebf8"/>
    <polygon points="0,808 447,850 447,854 0,812" fill="#ffffff"/>
    <polygon points="0,816 447,892 447,940 0,940" fill="#5e5f61"/>
  </svg>
  <header class="brand"><span class="brand__mark"></span><span class="brand__name">Tallowbrook Ventures</span></header>
  <p class="intro">A guiding hand,<br>a voice of reason,<br>a steady trusted partner<br>for success.</p>
  <p class="contact">0400 318 276<br>www.tallowbrookventures.com.au</p>
</section>

<section class="flyer flyer--back">
  <svg class="flyer__bg" viewBox="0 0 447 940" aria-hidden="true">
    <defs>
      <linearGradient id="hdrB" x1="0" x2="1"><stop offset="0" stop-color="#e3e4e6"/><stop offset=".55" stop-color="#ffffff"/><stop offset="1" stop-color="#e3e4e6"/></linearGradient>
      <linearGradient id="blueB" x1="0" y1="0" x2="1" y2="1"><stop offset="0" stop-color="#1c4789"/><stop offset="1" stop-color="#0c2757"/></linearGradient>
    </defs>
    <rect width="447" height="230" fill="url(#hdrB)"/>
    <polygon points="0,180 447,138 447,150 0,205" fill="#dcebf8"/>
    <polygon points="250,158 447,136 447,141 250,162" fill="#3a3b3d"/>
    <polygon points="0,203 447,141 447,858 0,810" fill="url(#blueB)"/>
    <polygon points="0,808 447,852 447,892 0,816" fill="#dcebf8"/>
    <polygon points="0,808 447,850 447,854 0,812" fill="#ffffff"/>
    <polygon points="0,816 447,892 447,940 0,940" fill="#5e5f61"/>
  </svg>
  <header class="brand"><span class="brand__mark"></span><span class="brand__name">Tallowbrook Ventures</span></header>
  <h2 class="services__title">OUR SERVICES</h2>
  <ul class="services__list">
    <li class="service"><svg class="service__icon" viewBox="0 0 36 36"><circle cx="18" cy="18" r="17" fill="#fff"/><circle cx="18" cy="20" r="8" fill="var(--icon-blue)"/><rect x="15" y="8" width="6" height="5" fill="var(--icon-blue)"/></svg>Taxation Compliance</li>
    <li class="service"><svg class="service__icon" viewBox="0 0 36 36"><circle cx="18" cy="18" r="17" fill="#fff"/><rect x="10" y="17" width="3" height="9" fill="var(--icon-blue)"/><rect x="15" y="11" width="3" height="15" fill="var(--icon-blue)"/><rect x="20" y="14" width="3" height="12" fill="var(--icon-blue)"/><rect x="25" y="18" width="2" height="8" fill="var(--icon-blue)"/></svg>Financial &amp; Management Reporting</li>
    <li class="service"><svg class="service__icon" viewBox="0 0 36 36"><circle cx="18" cy="18" r="17" fill="#fff"/><rect x="9" y="13" width="18" height="12" rx="2" fill="var(--icon-blue)"/><rect x="14" y="10" width="8" height="4" fill="none" stroke="var(--icon-blue)" stroke-width="2"/></svg>Self-Managed Superannuation</li>
    <li class="service"><svg class="service__icon" viewBox="0 0 36 36"><circle cx="18" cy="18" r="17" fill="#fff"/><circle cx="18" cy="14" r="5" fill="var(--icon-blue)"/><path d="M9 27c0-6 4-8 9-8s9 2 9 8z" fill="var(--icon-blue)"/></svg>Virtual CFO</li>
    <li class="service"><svg class="service__icon" viewBox="0 0 36 36"><circle cx="18" cy="18" r="17" fill="#fff"/><rect x="10" y="13" width="17" height="11" fill="var(--icon-blue)"/><polygon points="8,24 13,12 15,12 10,24" fill="var(--icon-blue)"/></svg>Business Planning</li>
    <li class="service"><svg class="service__icon" viewBox="0 0 36 36"><circle cx="18" cy="18" r="17" fill="#fff"/><rect x="9" y="10" width="18" height="12" fill="var(--icon-blue)"/><rect x="16" y="22" width="4" height="4" fill="var(--icon-blue)"/><rect x="13" y="26" width="10" height="2" fill="var(--icon-blue)"/></svg>KPIs &amp; Performance Monitoring</li>
    <li class="service"><svg class="service__icon" viewBox="0 0 36 36"><circle cx="18" cy="18" r="17" fill="#fff"/><path d="M9 13h7l2 2h9v11H9z" fill="var(--icon-blue)"/></svg>Succession Planning</li>
    <li class="service"><svg class="service__icon" viewBox="0 0 36 36"><circle cx="18" cy="18" r="17" fill="#fff"/><polygon points="8,19 18,10 28,19" fill="var(--icon-blue)"/><rect x="11" y="18" width="14" height="8" fill="var(--icon-blue)"/></svg>Estate Planning</li>
    <li class="service"><svg class="service__icon" viewBox="0 0 36 36"><circle cx="18" cy="18" r="17" fill="#fff"/><path d="M11 25a5 5 0 0 1 0-10 7 7 0 0 1 13-1 5.5 5.5 0 0 1 1 11z" fill="var(--icon-blue)"/></svg>Cloud Solutions</li>
    <li class="service"><svg class="service__icon" viewBox="0 0 36 36"><circle cx="18" cy="18" r="17" fill="#fff"/><ellipse cx="15" cy="16" rx="7" ry="5" fill="var(--icon-blue)"/><ellipse cx="22" cy="20" rx="6" ry="4.5" fill="var(--icon-blue)"/></svg>Business Support Services</li>
    <li class="service"><svg class="service__icon" viewBox="0 0 36 36"><circle cx="18" cy="18" r="17" fill="#fff"/><path d="M10 9h6v5a3 3 0 0 1-6 0z" fill="var(--icon-blue)"/><rect x="12.3" y="17" width="1.5" height="8" fill="var(--icon-blue)"/><path d="M20 9h6v5a3 3 0 0 1-6 0z" fill="var(--icon-blue)"/><rect x="22.3" y="17" width="1.5" height="8" fill="var(--icon-blue)"/></svg>The Wine Industry</li>
  </ul>
  <p class="contact">0400 318 276<br>www.tallowbrookventures.com.au</p>
</section>

</body>
</html>
```